Business Card Design

Consultation for design, construction athletic facilities specializing in synthetic turf systems and all weather running track systems.
Motto "True Owner Representation"
New Company that we'd like to highlight the LOGO first and foremost with the colors of the background and font as primary colors of the card too if possible. I've also attached a typical larger project design layout that could be used in the background to highlight our design and construction specialty.
Website is something we want very noticeable for driving traffic.
Target Market(s)
Athletic Directors, Designers, Government and Military, Contractors
Industry/Entity Type
Construction
Contact Information for Business Card
Peter L. Vandrell CFB, CTB
48317 W 63rd Ave
Harlow Ridge, WA 99482
C +1 503.555.0147
O +1 808.555.0182
Peter@fieldlaneco.example
www.fieldlaneco.example

```html
<!DOCTYPE html>
<html lang="en">
<head>
<meta charset="utf-8">
<title>Corvena Sport – Business Card</title>
<link rel="stylesheet" href="https://fonts.googleapis.com/css2?family=Carlito:wght@400;700&display=swap">
<style>
  :root {
    --bg: #d9d4cc;
    --card-black: #0a0a0a;
    --card-sheen: #262626;
    --gold: #e6a93a;
    --gold-soft: #b9842b;
    --gold-line: rgba(214, 160, 60, 0.35);
  }
  html, body {
    margin: 0;
    padding: 0;
    width: 1200px;
    height: 1023px;
    overflow: hidden;
    background: var(--bg);
    font-family: "Carlito", "Calibri", sans-serif;
  }
  .canvas {
    position: relative;
    width: 1200px;
    height: 1023px;
  }
  .card {
    position: absolute;
    width: 560px;
    height: 320px;
    background: linear-gradient(160deg, var(--card-sheen) 0%, var(--card-black) 45%, var(--card-black) 100%);
    border-radius: 4px;
    box-shadow: 0 10px 28px rgba(0,0,0,0.35);
    overflow: hidden;
  }
  .card--front { left: 70px; top: 150px; }
  .card--back  { left: 570px; top: 560px; }

  /* front */
  .site-plan {
    position: absolute;
    left: 150px;
    top: 40px;
    width: 330px;
    height: 220px;
    border: 1px solid var(--gold-line);
    border-radius: 60px;
    background: radial-gradient(ellipse at center, rgba(214,160,60,0.10), rgba(214,160,60,0.02) 70%);
  }
  .holder {
    position: absolute;
    right: 28px;
    top: 26px;
    text-align: right;
    color: var(--gold);
  }
  .holder__name {
    font-size: 30px;
    line-height: 1;
    margin: 0;
    font-weight: 400;
  }
  .holder__title {
    font-size: 13px;
    margin-top: 4px;
  }
  .contacts {
    position: absolute;
    right: 28px;
    top: 110px;
    list-style: none;
    margin: 0;
    padding: 0;
    color: var(--gold);
    font-size: 15px;
    text-align: right;
  }
  .contacts li {
    display: flex;
    justify-content: flex-end;
    align-items: center;
    gap: 8px;
    line-height: 24px;
  }
  .contacts .icon {
    width: 14px;
    height: 14px;
    flex: none;
  }
  .contacts .web { font-weight: 700; }
  .address {
    position: absolute;
    right: 28px;
    bottom: 24px;
    color: var(--gold);
    font-size: 14px;
    letter-spacing: 0.5px;
    text-transform: uppercase;
  }

  /* back */
  .brand {
    position: absolute;
    left: 0;
    right: 0;
    top: 120px;
    display: flex;
    flex-direction: column;
    align-items: center;
    color: var(--gold);
  }
  .brand__mark {
    width: 14px;
    height: 14px;
    border-radius: 50%;
    background: var(--gold);
    margin-bottom: 12px;
  }
  .brand__name {
    font-size: 34px;
    letter-spacing: 8px;
    line-height: 1;
  }
  .brand__sub {
    font-size: 20px;
    letter-spacing: 6px;
    margin-top: 4px;
  }
</style>
</head>
<body>
<main class="canvas">
  <section class="card card--front" aria-label="Card front">
    <div class="site-plan" role="img" aria-label="Faint site plan of an athletic field and running track"></div>
    <div class="holder">
      <h1 class="holder__name">Peter L. Vandrell CFB, CTB</h1>
      <div class="holder__title">Director</div>
    </div>
    <ul class="contacts">
      <li>+1 503.555.0147
        <svg class="icon" viewBox="0 0 14 14" aria-hidden="true"><circle cx="7" cy="7" r="7" fill="var(--gold)"/><path d="M4.5 3.5l1.5 0 .6 2-1 .7a5 5 0 0 0 2.2 2.2l.7-1 2 .6 0 1.5c-3.5 .3-6.3-2.5-6-6z" fill="var(--card-black)"/></svg></li>
      <li>+1 808.555.0182
        <svg class="icon" viewBox="0 0 14 14" aria-hidden="true"><circle cx="7" cy="7" r="7" fill="var(--gold)"/><path d="M4.5 3.5l1.5 0 .6 2-1 .7a5 5 0 0 0 2.2 2.2l.7-1 2 .6 0 1.5c-3.5 .3-6.3-2.5-6-6z" fill="var(--card-black)"/></svg></li>
      <li>Peter@fieldlaneco.example
        <svg class="icon" viewBox="0 0 14 14" aria-hidden="true"><circle cx="7" cy="7" r="7" fill="var(--gold)"/><rect x="3.5" y="4.5" width="7" height="5" fill="none" stroke="var(--card-black)" stroke-width="1"/><path d="M3.5 4.5l3.5 3 3.5-3" fill="none" stroke="var(--card-black)" stroke-width="1"/></svg></li>
      <li class="web">www.fieldlaneco.example
        <svg class="icon" viewBox="0 0 14 14" aria-hidden="true"><circle cx="7" cy="7" r="7" fill="var(--gold)"/><circle cx="7" cy="7" r="4" fill="none" stroke="var(--card-black)" stroke-width="1"/><path d="M3 7h8M7 3c-2 2.5-2 5.5 0 8M7 3c2 2.5 2 5.5 0 8" fill="none" stroke="var(--card-black)" stroke-width="0.8"/></svg></li>
    </ul>
    <div class="address">48317 W 63rd Ave Harlow Ridge, WA 99482</div>
  </section>

  <section class="card card--back" aria-label="Card back">
    <div class="brand">
      <span class="brand__mark" aria-hidden="true"></span>
      <span class="brand__name">CORVENA</span>
      <span class="brand__sub">sport</span>
    </div>
  </section>
</main>
</body>
</html>
```